Harbor Vantage needs new design business card

We are video surveillance and analytics software development company.
I am looking for a professional business card.
Our website is www.harborvantage-example.com.au
Please have a loo and get the feel for who we are and what we do.
I do not know what else to give you apart from good luck and I hope your design gets selected.
Thank you very much for participating
Industry/Entity Type
Business
Contact Information for Business Card
Address
27/14 Pemberly Street Millbrook NSW 2199
Telephone 1300 582 741
Mobile 0450 713 258
email: marcus@harborvantage-example.com.au
name
Marcus Felder
Position
Managing Director
Font styles to use
Other font styles liked:
- Arial
Look and feel

```html
<!DOCTYPE html>
<html lang="en">
<head>
<meta charset="utf-8">
<title>Harbor Vantage – Business Card</title>
<link href="https://fonts.googleapis.com/css2?family=Open+Sans:wght@400;600;700&display=swap" rel="stylesheet">
<style>
  :root {
    --navy: #173c6b;
    --slate: #627a88;
    --orange: #f7941d;
    --white: #ffffff;
    --page: #ece7df;
    --text-grey: #5d6b76;
  }
  html, body {
    margin: 0;
    padding: 0;
    width: 1200px;
    height: 1173px;
    overflow: hidden;
    background: var(--page);
    font-family: "Open Sans", Arial, sans-serif;
  }
  .canvas { position: relative; width: 1200px; height: 1173px; }

  .card {
    position: absolute;
    width: 906px;
    height: 519px;
    border-radius: 42px;
    overflow: hidden;
    box-shadow: 0 4px 14px rgba(0,0,0,0.18);
  }
  .card-front { left: 256px; top: 52px; background: var(--white); }
  .card-back { left: 47px; top: 617px; background: var(--slate); }

  .front-band {
    position: absolute;
    left: 0; right: 0; bottom: 0;
    height: 190px;
    background: var(--navy);
    border-top: 6px solid var(--orange);
  }

  .brand-name {
    position: absolute;
    left: 0; right: 0;
    top: 78px;
    display: flex;
    justify-content: center;
    align-items: center;
    gap: 22px;
    color: var(--navy);
    font-weight: 700;
    font-size: 64px;
    letter-spacing: 1px;
  }
  .brand-mark {
    width: 46px; height: 46px;
    background: var(--navy);
    border-radius: 6px;
  }

  .holder {
    position: absolute;
    left: 0; right: 0;
    top: 246px;
    margin: 0;
    text-align: center;
    color: var(--navy);
    white-space: nowrap;
  }
  .holder-name { font-weight: 700; font-size: 33px; }
  .holder-role { font-weight: 400; font-size: 22px; color: var(--text-grey); }

  .address {
    position: absolute;
    left: 66px;
    top: 432px;
    margin: 0;
    color: var(--white);
    font-size: 22px;
    line-height: 31px;
  }

  .contacts {
    position: absolute;
    right: 30px;
    top: 362px;
    margin: 0; padding: 0;
    list-style: none;
    color: var(--white);
    font-size: 22px;
    line-height: 36px;
    text-align: right;
  }
  .contacts li { display: flex; justify-content: flex-end; align-items: center; gap: 10px; }
  .contacts svg { width: 20px; height: 20px; fill: none; stroke: var(--white); stroke-width: 2; }

  .back-brand {
    position: absolute;
    left: 0; right: 0;
    top: 158px;
    text-align: center;
    color: var(--white);
    font-weight: 700;
    font-size: 70px;
    letter-spacing: 1px;
  }
  .back-url {
    position: absolute;
    left: 0; right: 0;
    top: 366px;
    text-align: center;
    color: var(--white);
    font-size: 27px;
    letter-spacing: 3px;
  }
</style>
</head>
<body>
<main class="canvas">

  <section class="card card-front" aria-label="Business card front">
    <div class="front-band"></div>

    <div class="brand-name"><span class="brand-mark"></span><span>Harbor Vantage</span></div>

    <p class="holder"><span class="holder-name">Marcus Felder,</span> <span class="holder-role">Managing Director</span></p>

    <p class="address">27/14 Pemberly Street<br>Millbrook NSW 2199</p>

    <ul class="contacts">
      <li>
        <svg viewBox="0 0 20 20" aria-hidden="true"><path d="M5 2 L8 6 L6 8 C7 11 9 13 12 14 L14 12 L18 15 L16 18 C9 18 2 11 2 4 Z"/></svg>
        <span>1300 582 741</span>
      </li>
      <li>
        <svg viewBox="0 0 20 20" aria-hidden="true"><rect x="5" y="1.5" width="10" height="17" rx="1.5"/><line x1="7" y1="5" x2="13" y2="5"/><line x1="8" y1="15" x2="12" y2="15"/></svg>
        <span>0450 713 258</span>
      </li>
      <li>
        <svg viewBox="0 0 20 20" aria-hidden="true"><rect x="2" y="5" width="16" height="11" rx="1"/><path d="M2 6 L10 12 L18 6"/></svg>
        <span>marcus@harborvantage-example.com.au</span>
      </li>
      <li>
        <svg viewBox="0 0 20 20" aria-hidden="true"><circle cx="10" cy="10" r="8"/><ellipse cx="10" cy="10" rx="3.5" ry="8"/><line x1="2" y1="10" x2="18" y2="10"/></svg>
        <span>www.harborvantage-example.com.au</span>
      </li>
    </ul>
  </section>

  <section class="card card-back" aria-label="Business card back">
    <div class="back-brand">Harbor Vantage</div>
    <div class="back-url">www.harborvantage-example.com.au</div>
  </section>

</main>
</body>
</html>
```